quorvaAgency Business Card Design Project

We need a business card design for quorvaAgency. quorvaAgency is an underwriting agency. Underwriting agencies act on behalf of insurers, to underwrite insurance. We will be operating in specialised classes of insurance initially and looking to expand from there. We would like to see designs that incorporate our logo colours as well as a contrasting stand out colour - also we'd like the logo itself to be embossed on the card.

Industry/Entity Type

Insurance

Requirements
Must have
• Logo on front
Nice to have
• Logo solely featured on back of card
Should not have
• Please do not use comic cans font :)

```html
<!DOCTYPE html>
<html lang="en">
<head>
<meta charset="utf-8">
<title>quorvaAgency Business Cards</title>
<link rel="stylesheet" href="https://fonts.googleapis.com/css2?family=Arimo:wght@400;700&display=swap">
<style>
  :root {
    --stage: #3c3f44;
    --silver-light: #f1f1f1;
    --silver-mid: #d9d9d9;
    --silver-dark: #c4c4c4;
    --ink: #3a3d42;
    --brand-blue: #1a5fb0;
    --back-blue: #1761b2;
    --emboss-blue: #12528f;
    --white: #ffffff;
    --muted: #5a5d62;
  }
  * { box-sizing: border-box; margin: 0; padding: 0; }
  html, body {
    width: 1200px;
    height: 900px;
    overflow: hidden;
    background: var(--stage);
    font-family: "Arimo", Arial, sans-serif;
  }
  .stage {
    position: relative;
    width: 1200px;
    height: 900px;
  }
  .card {
    position: absolute;
    width: 660px;
    height: 380px;
    box-shadow: 0 6px 18px rgba(0, 0, 0, 0.45);
  }
  /* Front */
  .card-front {
    left: 70px;
    top: 50px;
    background:
      repeating-linear-gradient(0deg, rgba(255,255,255,0.25) 0 1px, rgba(0,0,0,0.03) 1px 3px),
      linear-gradient(135deg, var(--silver-light), var(--silver-mid) 55%, var(--silver-dark));
  }
  .brand-mark {
    position: absolute;
    left: 50%;
    top: 40px;
    width: 120px;
    height: 120px;
    margin-left: -60px;
    border-radius: 50%;
    background: var(--brand-blue);
  }
  .brand-name {
    position: absolute;
    left: 0;
    right: 0;
    top: 168px;
    text-align: center;
    font-weight: 700;
    font-size: 76px;
    letter-spacing: -1px;
    color: var(--brand-blue);
    line-height: 1;
  }
  .holder {
    position: absolute;
    left: 92px;
    top: 282px;
    display: flex;
    align-items: center;
  }
  .holder-name {
    font-size: 34px;
    font-weight: 700;
    color: var(--ink);
    letter-spacing: -0.5px;
  }
  .holder-name .surname { color: var(--brand-blue); }
  .holder-divider {
    width: 2px;
    height: 40px;
    background: var(--muted);
    margin: 0 16px 0 18px;
  }
  .holder-role {
    font-size: 19px;
    color: var(--muted);
  }
  /* Back */
  .card-back {
    left: 470px;
    top: 470px;
    background: var(--back-blue);
  }
  .emboss-mark {
    position: absolute;
    left: 50%;
    top: 36px;
    width: 120px;
    height: 120px;
    margin-left: -60px;
    border-radius: 50%;
    background: var(--emboss-blue);
  }
  .emboss-name {
    position: absolute;
    left: 0;
    right: 0;
    top: 172px;
    text-align: center;
    font-weight: 700;
    font-size: 76px;
    letter-spacing: -1px;
    color: var(--emboss-blue);
    line-height: 1;
  }
  .contact {
    position: absolute;
    left: 40px;
    bottom: 34px;
    color: var(--white);
    font-size: 17px;
    font-weight: 700;
    line-height: 1.55;
  }
  .contact .row-second { padding-left: 120px; }
  .contact .value { font-weight: 400; }
  .contact .gap { display: inline-block; width: 20px; }
</style>
</head>
<body>
<main class="stage">
  <section class="card card-front" aria-label="Card front">
    <div class="brand-mark" aria-hidden="true"></div>
    <div class="brand-name">quorvaAgency</div>
    <div class="holder">
      <span class="holder-name">marcus<span class="surname">Hale</span></span>
      <span class="holder-divider" aria-hidden="true"></span>
      <span class="holder-role">Managing Director</span>
    </div>
  </section>

  <section class="card card-back" aria-label="Card back">
    <div class="emboss-mark" aria-hidden="true"></div>
    <div class="emboss-name">quorvaAgency</div>
    <div class="contact">
      <p>Mobile: XXXXXX XXXXX<span class="gap"></span>Work: XXXXXX XXXXX <span class="value">ex.XXX</span></p>
      <p class="row-second">Email: XXXXXX@XXXXXXXXXXX</p>
    </div>
  </section>
</main>
</body>
</html>
```